The Lantern Whiskey & Coffee - Bar Menu

The Lantern is a speakeasy style coffee and whiskey bar. Upscale with design elements tying in both prohibition era elegance and modern touches.

Black and Gold are our colors. (see logo)

We would need a 8 page menu- front and back. 4.24 in x 11 in for each page. The pages would be:

Intro page
Food/Dessert
Cocktails x 2 pages
Wine- Glass Pour
Wine- Bottle only
Beer
Non-Alcoholic Beverages

Attached is the menu cocktails and food/non alcoholic.

We need an editable format as this menu would be constantly changing.

UPDATE: The owner would potentially like to see the use of the original floor plans incorporated into the menu design. I have uploaded those to this brief.

UPDATE: I have added some photos that show the style the owner would like the writing to be displayed.

Requirements
Should not have
• No pictures of wine or beer or other images. Clipart could be fine, but we want to showcase class and an upscale vibe.

```html
<!DOCTYPE html>
<html lang="en">
<head>
<meta charset="utf-8">
<title>The Lantern Whiskey &amp; Coffee – Bar Menu</title>
<link href="https://fonts.googleapis.com/css2?family=Federo&family=Barlow+Condensed:wght@300;400;500;600&display=swap" rel="stylesheet">
<style>
:root{
  --backdrop:#e9e9ea;
  --ink:#0b0b0b;
  --panel:#101010;
  --gold:#d6a93a;
  --gold-soft:#b8923a;
  --white:#f2f2f2;
  --rule:#5a5a5a;
}
*{margin:0;padding:0;box-sizing:border-box}
html,body{width:1200px;height:1000px;overflow:hidden;background:var(--backdrop)}
body{position:relative;font-family:"Barlow Condensed",sans-serif;color:var(--white)}

.page{position:absolute;background:var(--panel)}
.cocktail-page{left:51px;top:40px;width:356px;height:923px;
  background:linear-gradient(180deg,#0c0c0c 0%,#1c1c1c 45%,#0e0e0e 100%)}
.spread{left:407px;top:18px;width:739px;height:962px;overflow:hidden}
.spread-photo{position:absolute;inset:0;
  background:radial-gradient(ellipse at 70% 55%,#3a3a3a 0%,#1d1d1d 45%,#0b0b0b 100%)}
.fold{position:absolute;left:370px;top:0;width:1px;height:100%;background:#3a3020}

.page-title{position:absolute;font-family:"Federo",sans-serif;color:var(--gold);letter-spacing:1px}
.cocktail-page .page-title{left:32px;top:37px;width:117px;font-size:21px;line-height:33px;
  border-top:1px solid var(--gold-soft);border-bottom:1px solid var(--gold-soft)}

.spirit-bar{position:absolute;left:31px;width:294px;height:17px;border:1px solid var(--gold-soft);
  font-family:"Federo",sans-serif;color:var(--gold);font-size:13px;line-height:15px;padding-left:6px;letter-spacing:1px}

.drink{position:absolute;left:32px;width:290px}
.drink-name{font-size:11px;font-weight:500;line-height:13px;text-transform:uppercase;color:var(--white)}
.drink-desc{font-size:9.5px;font-weight:300;line-height:12px;color:var(--gold);margin-top:4px}
.divider{position:absolute;left:32px;width:292px;border-top:1px dashed var(--rule)}

.banner{position:absolute;left:134px;top:0;width:100px;height:135px}
.brand-name{position:absolute;left:134px;top:80px;width:100px;text-align:center;
  font-family:"Barlow Condensed",sans-serif;font-weight:600;font-size:16px;color:var(--gold);letter-spacing:1px}

.ornament-rule{position:absolute;left:76px;width:219px;height:9px}
.house-notes{position:absolute;left:66px;top:370px;width:238px;text-align:center;
  font-size:10.5px;font-weight:300;line-height:14.5px;color:var(--gold)}
.house-notes p{margin-bottom:14px}
.building{position:absolute;left:71px;top:755px;width:219px;height:155px;
  background:linear-gradient(180deg,rgba(214,169,58,.18),rgba(214,169,58,.32))}
.ground-line{position:absolute;left:21px;top:910px;width:324px;border-top:1px solid var(--gold-soft)}

.section-head{position:absolute;left:401px;width:304px;border-top:1px solid var(--gold-soft);border-bottom:1px solid var(--gold-soft);
  font-family:"Federo",sans-serif;font-size:21px;line-height:31px;color:var(--gold);padding-left:7px;letter-spacing:1px}
.dish{position:absolute;left:407px;width:300px}
.dish-row{display:flex;justify-content:space-between;font-size:13.5px;font-weight:500;line-height:15px;text-transform:uppercase}
.dish-desc{font-size:9.5px;font-weight:300;line-height:11px;color:var(--gold);white-space:nowrap}
.dish-divider{position:absolute;left:407px;width:300px;border-top:1px dashed var(--rule)}
</style>
</head>
<body>

<section class="page cocktail-page">
  <h2 class="page-title" style="top:37px">COCKTAILS</h2>

  <div class="spirit-bar" style="top:107px">VODKA</div>
  <div class="drink" style="top:135px"><div class="drink-name">The Affair</div><div class="drink-desc">Vodka (strawberry/orange infusion), Lemon Oleo Saccahrum,<br>PeaFlower Gin Float(Blue) (N&amp;N).</div></div>
  <div class="divider" style="top:185px"></div>
  <div class="drink" style="top:196px"><div class="drink-name">Bootleggers Gold</div><div class="drink-desc">Vodka, Yellow Chartrelle, Pineapple, Lime Juice, Simple Syrup,<br>Lemon Zest.</div></div>

  <div class="spirit-bar" style="top:253px">TEQUILA</div>
  <div class="drink" style="top:282px"><div class="drink-name">The Mayan</div><div class="drink-desc">Casa Alta Blanco, Raicilla (non-peaty Mezcal), Green Chartrelle,<br>Pistachio Liqueur, Olive, Lime.</div></div>
  <div class="divider" style="top:335px"></div>
  <div class="drink" style="top:347px"><div class="drink-name">Toreador*</div><div class="drink-desc">Blanco, Mezcal, Apricot Cordial, Lime Juice, GrapeFruit oil(oleo),<br>Mezcal Mist.</div></div>

  <div class="spirit-bar" style="top:402px">RUM</div>
  <div class="drink" style="top:432px"><div class="drink-name">Smugglers Cove**</div><div class="drink-desc">Rum (Cuban), Pomegranite Liqueur, Lemon Juice,<br>Macadamia Orgeat, Cocoa Bitters (Eggwhite).</div></div>
  <div class="divider" style="top:483px"></div>
  <div class="drink" style="top:496px"><div class="drink-name">Mary Pickwell*</div><div class="drink-desc">Rum (Blanco Cuban), Pineapple, Maraschino Liqueur, Grenadine.</div></div>
  <div class="divider" style="top:537px"></div>
  <div class="drink" style="top:550px"><div class="drink-name">Ray Rum Runner (Local)</div><div class="drink-desc">Rum (Blanco), Rhum Agricole (non-peat Mezcal) Lime Juice,<br>Simple Syrup w/in season fruit.</div></div>

  <div class="spirit-bar" style="top:609px">GIN</div>
  <div class="drink" style="top:642px"><div class="drink-name">Clover Club*</div><div class="drink-desc">Bluestone Gin, Rasperry Liquor, Lemon Juice, Raspberries,<br>Vanilla, Prosecco, Milk (Clarified).</div></div>
  <div class="divider" style="top:694px"></div>
  <div class="drink" style="top:710px"><div class="drink-name">Clover Club#2*</div><div class="drink-desc">Gin, Noirelle Vermouth, Raspberry, Lemon Juice, EggWhite.</div></div>
  <div class="divider" style="top:752px"></div>
  <div class="drink" style="top:767px"><div class="drink-name">Limonata</div><div class="drink-desc">Gin (Lemon infused), Limoncello, Lemon Curd, Lemon Juice,<br>San Bellino Limonata.</div></div>
  <div class="divider" style="top:820px"></div>
  <div class="drink" style="top:835px"><div class="drink-name">Colony Cocktail</div><div class="drink-desc">Gin, Pink Grapefruit, Maraschino Liqueur, Grapefruit twist.</div></div>
</section>

<section class="page spread">
  <div class="spread-photo" role="img" aria-label="Soft, darkened photograph of the bar interior behind the menu text"></div>
  <div class="fold"></div>

  <svg class="banner" viewBox="0 0 100 135" aria-hidden="true">
    <polygon points="0,0 100,0 100,112 50,135 0,112" fill="#1a1a1a"/>
  </svg>
  <div class="brand-name">THE LANTERN</div>

  <svg class="ornament-rule" style="top:306px" viewBox="0 0 219 9" aria-hidden="true">
    <line x1="0" y1="4.5" x2="97" y2="4.5" stroke="#b8923a"/>
    <circle cx="109.5" cy="4.5" r="2" fill="#d6a93a"/>
    <line x1="122" y1="4.5" x2="219" y2="4.5" stroke="#b8923a"/>
  </svg>
  <div class="house-notes">
    <p>• The Lantern Whiskey &amp; Coffee Reserves the right to change menus selections, and/or the prices that accompany those items, as they appear on the menus at the restaurant.</p>
    <p>• Only one promotion/special/discount/kickback may be used at one time, per table or check.</p>
    <p>• 20% service charged added onto bills of parties of 6 or more.</p>
  </div>
  <svg class="ornament-rule" style="top:596px" viewBox="0 0 219 9" aria-hidden="true">
    <line x1="0" y1="4.5" x2="97" y2="4.5" stroke="#b8923a"/>
    <circle cx="109.5" cy="4.5" r="2" fill="#d6a93a"/>
    <line x1="122" y1="4.5" x2="219" y2="4.5" stroke="#b8923a"/>
  </svg>
  <div class="building" role="img" aria-label="Gold line drawing of the bar's building facade"></div>
  <div class="ground-line"></div>

  <h2 class="section-head" style="top:175px">FOOD</h2>
  <div class="dish" style="top:225px"><div class="dish-row"><span>Bone Marrow</span><span>$20</span></div><div class="dish-desc">Bone marrow roasted with sea salt and served with warm tortillas.</div></div>
  <div class="dish-divider" style="top:262px"></div>
  <div class="dish" style="top:272px"><div class="dish-row"><span>Charcuterie Board</span><span>$25</span></div><div class="dish-desc">Assorted artisan meats and cheeses, nuts, and fruits.</div></div>
  <div class="dish-divider" style="top:308px"></div>
  <div class="dish" style="top:318px"><div class="dish-row"><span>Hummus, Veggie &amp; Pita</span><span>$16</span></div><div class="dish-desc">Assorted vegetables with warm pita and roasted garlic hummus.</div></div>
  <div class="dish-divider" style="top:354px"></div>
  <div class="dish" style="top:364px"><div class="dish-row"><span>Lamb Chops</span><span>$18</span></div><div class="dish-desc">Lamb chops broiled with rosemary.</div></div>
  <div class="dish-divider" style="top:398px"></div>
  <div class="dish" style="top:406px"><div class="dish-row"><span>Tuna Tower</span><span>$17</span></div><div class="dish-desc">Fresh tuna served with white rice, avocado and spice.</div></div>
  <div class="dish-divider" style="top:442px"></div>
  <div class="dish" style="top:451px"><div class="dish-row"><span>Lettuce Wrap- Walnut Shrimp</span><span>$13</span></div><div class="dish-desc">Honey walnut aioli coated shrimp and lettuce cups with a candied walnut.</div></div>

  <h2 class="section-head" style="top:563px">DESSERTS</h2>
  <div class="dish" style="top:613px"><div class="dish-row"><span>Tart</span><span></span></div><div class="dish-desc">Your choice of apple or berry with vanilla ice cream.</div></div>
  <div class="dish-divider" style="top:651px"></div>
  <div class="dish" style="top:661px"><div class="dish-row"><span>Cheesecake</span><span></span></div><div class="dish-desc">Chocolate or strawberry drizzle.</div></div>
</section>

</body>
</html>
```